Powerpoint Sales and Pre-Sales Decks

We need a GD to support us as we start buillidng many PPT decks - we are a start-up based in London in the Telecomms space

```html
<!DOCTYPE html>
<html lang="en">
<head>
<meta charset="utf-8">
<title>Sales and Pre-Sales Deck Templates</title>
<link href="https://fonts.googleapis.com/css2?family=Lato:wght@300;400;700&display=swap" rel="stylesheet">
<style>
:root{
  --canvas:#eeeeee;
  --navy:#2c3340;
  --band:#4b5468;
  --blue:#4a7fb5;
  --green:#6dbf96;
  --lime:#9bc23c;
  --orange:#e9863a;
  --red:#c9452e;
  --ink:#333a44;
  --muted:#8a8f97;
}
*{margin:0;padding:0;box-sizing:border-box}
html,body{width:1200px;height:4419px;overflow:hidden;background:var(--canvas);font-family:'Lato',sans-serif}
.slide{position:absolute;width:565px;height:318px;background:#fff;overflow:hidden}
.slide.dark{background:var(--navy)}
.num{position:absolute;top:8px;right:10px;background:#9aa0aa;color:#fff;font-size:6px;padding:1px 3px;border-radius:2px}
.title{position:absolute;top:20px;left:0;right:0;text-align:center;font-size:14px;color:var(--ink)}
.title.light,.dark .title{color:#fff}
.sub{position:absolute;top:38px;left:0;right:0;text-align:center;font-size:6px;color:var(--green)}
.p{font-size:5.5px;line-height:1.55;color:var(--muted)}
.dark .p{color:#c9ccd2}
.abs{position:absolute}
.ph{position:absolute;border-radius:3px}
.map{background:linear-gradient(160deg,#e4e6e8,#d3d6da)}
.ic{position:absolute;width:18px;height:18px;border-radius:50%}
.h{font-size:7px;color:var(--ink);font-weight:700}
.dark .h{color:#fff}
.sec-title{position:absolute;left:36px;top:150px;color:#fff;font-size:15px}
.sec-sub{position:absolute;left:36px;top:170px;color:var(--blue);font-size:6px}
.sec-p{position:absolute;left:36px;top:182px;width:300px}
.sec-icon{position:absolute;left:36px;top:118px;width:24px;height:24px}
.center{text-align:center}
.strip-word{font-size:22px;font-weight:300;padding-left:4px;line-height:30px;white-space:nowrap}
</style>
</head>
<body>

<section class="slide" style="left:22px;top:20px">
  <div class="num">27</div>
  <div class="title">Arrow picture callout</div>
  <div class="sub">Subtitle Example</div>
  <div class="ph" role="img" aria-label="Photo thumbnail" style="left:36px;top:88px;width:70px;height:44px;background:linear-gradient(#5d6b85,#3b4559)"></div>
  <div class="ph" role="img" aria-label="Photo thumbnail" style="left:36px;top:200px;width:70px;height:44px;background:linear-gradient(#5d6b85,#3b4559)"></div>
  <svg class="abs" style="left:0;top:0" width="565" height="318">
    <g fill="#8e939b">
      <polygon points="138,105 146,110 138,115"/><polygon points="276,105 284,110 276,115"/><polygon points="410,105 418,110 410,115"/>
      <polygon points="138,217 146,222 138,227"/><polygon points="276,217 284,222 276,227"/><polygon points="410,217 418,222 410,227"/>
      <rect x="130" y="108" width="8" height="4"/><rect x="268" y="108" width="8" height="4"/><rect x="402" y="108" width="8" height="4"/>
      <rect x="130" y="220" width="8" height="4"/><rect x="268" y="220" width="8" height="4"/><rect x="402" y="220" width="8" height="4"/>
    </g>
  </svg>
  <p class="p abs" style="left:170px;top:76px;width:90px">Donec vel nisl nec risus vulputate placerat in at ligula. Donec auctor magna nec lacus porttitor hendrerit. In pulvinar quam vitae pellentesque aliquam. Fusce venenatis lorem faucibus.</p>
  <p class="p abs" style="left:300px;top:76px;width:90px">Donec vel nisl nec risus vulputate placerat in at ligula. Donec auctor magna nec lacus porttitor hendrerit. In pulvinar quam vitae pellentesque aliquam. Fusce venenatis lorem faucibus.</p>
  <p class="p abs" style="left:430px;top:76px;width:90px">Donec vel nisl nec risus vulputate placerat in at ligula. Donec auctor magna nec lacus porttitor hendrerit. In pulvinar quam vitae pellentesque aliquam. Fusce venenatis lorem faucibus.</p>
  <p class="p abs" style="left:170px;top:188px;width:90px">Donec vel nisl nec risus vulputate placerat in at ligula. Donec auctor magna nec lacus porttitor hendrerit. In pulvinar quam vitae pellentesque aliquam. Fusce venenatis lorem faucibus.</p>
  <p class="p abs" style="left:300px;top:188px;width:90px">Donec vel nisl nec risus vulputate placerat in at ligula. Donec auctor magna nec lacus porttitor hendrerit. In pulvinar quam vitae pellentesque aliquam. Fusce venenatis lorem faucibus.</p>
  <p class="p abs" style="left:430px;top:188px;width:90px">Donec vel nisl nec risus vulputate placerat in at ligula. Donec auctor magna nec lacus porttitor hendrerit. In pulvinar quam vitae pellentesque aliquam. Fusce venenatis lorem faucibus.</p>
</section>

<section class="slide dark" style="left:612px;top:20px">
  <div class="num">28</div>
  <svg class="abs" style="left:0;top:0" width="565" height="318"><polygon points="360,318 395,318 565,40 565,0 555,0" fill="var(--green)"/><polygon points="400,318 430,318 565,110 565,60" fill="var(--blue)"/></svg>
  <svg class="sec-icon" viewBox="0 0 24 24"><circle cx="12" cy="12" r="11" fill="#fff"/><path d="M7 8c3 0 4 2 3 4s2 3 1 6M14 5c1 2 4 2 4 5" stroke="var(--navy)" stroke-width="2" fill="none"/></svg>
  <div class="sec-title">Map Section</div>
  <div class="sec-sub">Subtitle Example Here</div>
  <p class="p sec-p">Donec vel nisl nec risus vulputate placerat in at ligula. Donec auctor magna nec lacus porttitor hendrerit. In pulvinar quam vitae pellentesque aliquam. Fusce venenatis lorem faucibus, commodo magna eget, egestas orci.</p>
</section>

<section class="slide" style="left:22px;top:360px">
  <div class="num">29</div>
  <div class="title">United State Transaction</div>
  <div class="sub">Subtitle Example</div>
  <div class="ph" role="img" aria-label="Map of the United States with highlighted states" style="left:50px;top:55px;width:280px;height:150px;background:linear-gradient(150deg,#4b5468 55%,#4a7fb5 70%,#6dbf96 85%,#9bc23c)"></div>
  <svg class="abs" style="left:375px;top:60px" width="130" height="100">
    <g stroke="#e2e4e7" stroke-width=".5"><line x1="0" y1="10" x2="130" y2="10"/><line x1="0" y1="35" x2="130" y2="35"/><line x1="0" y1="60" x2="130" y2="60"/><line x1="0" y1="85" x2="130" y2="85"/></g>
    <g fill="var(--navy)"><rect x="40" y="55" width="11" height="30"/><rect x="58" y="40" width="11" height="45"/><rect x="76" y="28" width="11" height="57"/><rect x="94" y="18" width="11" height="67"/></g>
  </svg>
  <div class="h abs" style="left:390px;top:173px;font-size:6px">Subtitle Example</div>
  <p class="p abs" style="left:390px;top:183px;width:165px">Donec vel nisl nec risus vulputate placerat in at ligula. Donec auctor magna nec lacus porttitor hendrerit. In pulvinar quam vitae.</p>
  <div class="abs" style="left:50px;top:250px;width:130px"><div class="h" style="color:var(--blue);font-size:6px">● Subtitle Example</div><p class="p">Donec vel nisl nec risus vulputate placerat in at ligula auctor magna nec lacus porttitor hendrerit.</p></div>
  <div class="abs" style="left:205px;top:250px;width:130px"><div class="h" style="color:var(--green);font-size:6px">● Subtitle Example</div><p class="p">Donec vel nisl nec risus vulputate placerat in at ligula auctor magna nec lacus porttitor hendrerit.</p></div>
  <div class="abs" style="left:360px;top:250px;width:130px"><div class="h" style="color:var(--lime);font-size:6px">● Subtitle Example</div><p class="p">Donec vel nisl nec risus vulputate placerat in at ligula auctor magna nec lacus porttitor hendrerit.</p></div>
</section>

<section class="slide" style="left:612px;top:360px">
  <div class="num">30</div>
  <div class="title">Europe Transaction</div>
  <div class="sub">Subtitle Example</div>
  <div class="ph" role="img" aria-label="Map of Europe with highlighted countries" style="left:50px;top:55px;width:280px;height:150px;background:radial-gradient(circle at 45% 50%,#4b5468 20%,#6dbf96 35%,#d9dcdf 55%)"></div>
  <svg class="abs" style="left:375px;top:60px" width="130" height="100">
    <g stroke="#e2e4e7" stroke-width=".5"><line x1="0" y1="10" x2="130" y2="10"/><line x1="0" y1="35" x2="130" y2="35"/><line x1="0" y1="60" x2="130" y2="60"/><line x1="0" y1="85" x2="130" y2="85"/></g>
    <g fill="var(--navy)"><rect x="40" y="55" width="11" height="30"/><rect x="58" y="40" width="11" height="45"/><rect x="76" y="28" width="11" height="57"/><rect x="94" y="18" width="11" height="67"/></g>
  </svg>
  <div class="h abs" style="left:390px;top:173px;font-size:6px">Subtitle Example</div>
  <p class="p abs" style="left:390px;top:183px;width:165px">Donec vel nisl nec risus vulputate placerat in at ligula. Donec auctor magna nec lacus porttitor hendrerit. In pulvinar quam vitae.</p>
  <div class="abs" style="left:50px;top:250px;width:130px"><div class="h" style="color:var(--blue);font-size:6px">● Subtitle Example</div><p class="p">Donec vel nisl nec risus vulputate placerat in at ligula auctor magna nec lacus porttitor hendrerit.</p></div>
  <div class="abs" style="left:205px;top:250px;width:130px"><div class="h" style="color:var(--green);font-size:6px">● Subtitle Example</div><p class="p">Donec vel nisl nec risus vulputate placerat in at ligula auctor magna nec lacus porttitor hendrerit.</p></div>
  <div class="abs" style="left:360px;top:250px;width:130px"><div class="h" style="color:var(--lime);font-size:6px">● Subtitle Example</div><p class="p">Donec vel nisl nec risus vulputate placerat in at ligula auctor magna nec lacus porttitor hendrerit.</p></div>
</section>

<section class="slide" style="left:22px;top:700px">
  <div class="num">31</div>
  <div class="title">America Transaction</div>
  <div class="sub">Subtitle Example</div>
  <div class="ph" role="img" aria-label="Map of the Americas with highlighted regions" style="left:50px;top:55px;width:280px;height:150px;background:linear-gradient(170deg,#4b5468 25%,#6dbf96 40%,#4a7fb5 55%,#9bc23c 68%,#d9dcdf 75%)"></div>
  <svg class="abs" style="left:375px;top:60px" width="130" height="100">
    <g stroke="#e2e4e7" stroke-width=".5"><line x1="0" y1="10" x2="130" y2="10"/><line x1="0" y1="35" x2="130" y2="35"/><line x1="0" y1="60" x2="130" y2="60"/><line x1="0" y1="85" x2="130" y2="85"/></g>
    <g fill="var(--navy)"><rect x="40" y="55" width="11" height="30"/><rect x="58" y="40" width="11" height="45"/><rect x="76" y="28" width="11" height="57"/><rect x="94" y="18" width="11" height="67"/></g>
  </svg>
  <div class="h abs" style="left:390px;top:173px;font-size:6px">Subtitle Example</div>
  <p class="p abs" style="left:390px;top:183px;width:165px">Donec vel nisl nec risus vulputate placerat in at ligula. Donec auctor magna nec lacus porttitor hendrerit. In pulvinar quam vitae.</p>
  <div class="abs" style="left:50px;top:250px;width:130px"><div class="h" style="color:var(--blue);font-size:6px">● Subtitle Example</div><p class="p">Donec vel nisl nec risus vulputate placerat in at ligula auctor magna nec lacus porttitor hendrerit.</p></div>
  <div class="abs" style="left:205px;top:250px;width:130px"><div class="h" style="color:var(--green);font-size:6px">● Subtitle Example</div><p class="p">Donec vel nisl nec risus vulputate placerat in at ligula auctor magna nec lacus porttitor hendrerit.</p></div>
  <div class="abs" style="left:360px;top:250px;width:130px"><div class="h" style="color:var(--lime);font-size:6px">● Subtitle Example</div><p class="p">Donec vel nisl nec risus vulputate placerat in at ligula auctor magna nec lacus porttitor hendrerit.</p></div>
</section>

<section class="slide dark" style="left:612px;top:700px">
  <div class="num">32</div>
  <div class="abs strip-word" style="left:28px;top:100px;width:195px;height:30px;background:var(--green);color:#b6e3cc">THE BEST WAY</div>
  <div class="abs" style="left:228px;top:100px;width:285px;height:30px;background:var(--blue)"></div>
  <div class="abs strip-word" style="left:28px;top:136px;width:130px;height:30px;background:var(--blue);color:#9fc2e6">TO CLOSE</div>
  <div class="abs" style="left:163px;top:136px;width:350px;height:30px;background:var(--green);padding:6px 10px"><p class="p" style="color:#fff;text-align:right">Donec vel nisl nec risus vulputate placerat in at ligula. Donec auctor magna nec lacus porttitor hendrerit. In pulvinar quam vitae pellentesque aliquam.</p></div>
  <div class="abs strip-word" style="left:28px;top:172px;width:210px;height:30px;background:var(--lime);color:#d3e79a">YOUR BUSINESS</div>
  <div class="abs" style="left:243px;top:172px;width:270px;height:30px;background:var(--blue)"></div>
</section>

<section class="slide" style="left:22px;top:1040px">
  <div class="num">33</div>
  <div class="title">Australia Sales by gender</div>
  <div class="sub">Subtitle Example</div>
  <div class="ph map" role="img" aria-label="World map background" style="left:40px;top:55px;width:485px;height:210px"></div>
  <svg class="abs" style="left:0;top:0" width="565" height="318"><circle cx="235" cy="120" r="48" fill="var(--green)" opacity=".85"/><circle cx="275" cy="160" r="62" fill="var(--orange)" opacity=".9"/></svg>
  <div class="abs" style="left:40px;top:105px;font-size:8px;color:var(--orange);font-weight:700">Australia</div>
  <div class="abs" style="left:40px;top:118px;font-size:9px;color:var(--orange)">76%</div>
  <div class="abs" style="left:65px;top:118px;width:80px"><div class="h" style="font-size:6px">Female</div><p class="p">Lorem ipsum dolor sit amet, consectetur adipiscing elit.</p></div>
  <div class="abs" style="left:40px;top:170px;font-size:9px;color:var(--green)">24%</div>
  <div class="abs" style="left:65px;top:170px;width:80px"><div class="h" style="font-size:6px">Male</div><p class="p">Lorem ipsum dolor sit amet, consectetur adipiscing elit.</p></div>
  <div class="abs" style="left:425px;top:108px;width:100px"><div class="h" style="font-size:6px">Region A</div><p class="p">Lorem ipsum dolor sit amet, consectetur adipiscing elit. Integer mollis vehicula ligula.</p></div>
  <div class="abs" style="left:425px;top:155px;width:100px"><div class="h" style="font-size:6px">Region B</div><p class="p">Lorem ipsum dolor sit amet, consectetur adipiscing elit. Integer mollis vehicula ligula.</p></div>
  <p class="p abs" style="left:40px;top:278px;width:485px">Donec vel nisl nec risus vulputate placerat in at ligula. Donec auctor magna nec lacus porttitor hendrerit. In pulvinar quam vitae pellentesque aliquam. Fusce venenatis lorem faucibus, commodo magna eget, egestas orci. Nullam at risus congue, hendrerit enim.</p>
</section>

<section class="slide" style="left:612px;top:1040px">
  <div class="num">34</div>
  <div class="title">Canada Sales by gender</div>
  <div class="sub">Subtitle Example</div>
  <div class="ph map" role="img" aria-label="World map background with Canada highlighted" style="left:40px;top:55px;width:485px;height:210px"></div>
  <svg class="abs" style="left:0;top:0" width="565" height="318"><circle cx="295" cy="130" r="62" fill="var(--green)" opacity=".85"/><circle cx="245" cy="172" r="48" fill="var(--orange)" opacity=".9"/></svg>
  <div class="abs" style="left:40px;top:105px;font-size:8px;color:var(--orange);font-weight:700">Canada</div>
  <div class="abs" style="left:40px;top:118px;font-size:9px;color:var(--orange)">76%</div>
  <div class="abs" style="left:65px;top:118px;width:80px"><div class="h" style="font-size:6px">Female</div><p class="p">Lorem ipsum dolor sit amet, consectetur adipiscing elit.</p></div>
  <div class="abs" style="left:40px;top:170px;font-size:9px;color:var(--green)">24%</div>
  <div class="abs" style="left:65px;top:170px;width:80px"><div class="h" style="font-size:6px">Male</div><p class="p">Lorem ipsum dolor sit amet, consectetur adipiscing elit.</p></div>
  <div class="abs" style="left:425px;top:108px;width:100px"><div class="h" style="font-size:6px">Region A</div><p class="p">Lorem ipsum dolor sit amet, consectetur adipiscing elit. Integer mollis vehicula ligula.</p></div>
  <div class="abs" style="left:425px;top:155px;width:100px"><div class="h" style="font-size:6px">Region B</div><p class="p">Lorem ipsum dolor sit amet, consectetur adipiscing elit. Integer mollis vehicula ligula.</p></div>
  <p class="p abs" style="left:40px;top:278px;width:485px">Donec vel nisl nec risus vulputate placerat in at ligula. Donec auctor magna nec lacus porttitor hendrerit. In pulvinar quam vitae pellentesque aliquam. Fusce venenatis lorem faucibus, commodo magna eget, egestas orci. Nullam at risus congue, hendrerit enim.</p>
</section>

<section class="slide" style="left:22px;top:1380px">
  <div class="num">35</div>
  <div class="title">Worldwide Social Networks</div>
  <div class="sub">Subtitle Example</div>
  <div class="ph map" role="img" aria-label="World map background" style="left:40px;top:55px;width:485px;height:220px"></div>
  <svg class="abs" style="left:0;top:0" width="565" height="318"><circle cx="140" cy="165" r="82" fill="var(--blue)" opacity=".9"/><circle cx="282" cy="165" r="82" fill="var(--lime)" opacity=".9"/><circle cx="424" cy="165" r="82" fill="var(--red)" opacity=".9"/></svg>
  <div class="abs center" style="left:80px;top:145px;width:120px;color:#fff"><div style="font-size:8px">Chirpnet</div><p class="p" style="color:#eef">Lorem ipsum dolor sit amet, consectetur adipiscing elit. Integer mollis vehicula ligula.</p><div style="font-size:9px;margin-top:4px">25.345 Posts</div></div>
  <div class="abs center" style="left:222px;top:145px;width:120px;color:#fff"><div style="font-size:8px">Snapframe</div><p class="p" style="color:#f4f8e8">Lorem ipsum dolor sit amet, consectetur adipiscing elit. Integer mollis vehicula ligula.</p><div style="font-size:9px;margin-top:4px">983 Shares</div></div>
  <div class="abs center" style="left:364px;top:145px;width:120px;color:#fff"><div style="font-size:8px">Circlebook</div><p class="p" style="color:#fbe">Lorem ipsum dolor sit amet, consectetur adipiscing elit. Integer mollis vehicula ligula.</p><div style="font-size:9px;margin-top:4px">134.984 Likes</div></div>
</section>

<section class="slide" style="left:612px;top:1380px">
  <div class="num">36</div>
  <div class="title">Worldwide Transaction</div>
  <div class="sub">Subtitle Example</div>
  <div class="ph" role="img" aria-label="World map in grey with highlighted countries" style="left:40px;top:60px;width:485px;height:220px;background:linear-gradient(160deg,#bfc3c8,#d5d8dc)"></div>
  <svg class="abs" style="left:0;top:0" width="565" height="318">
    <rect x="100" y="140" width="40" height="22" fill="var(--blue)"/><rect x="150" y="200" width="18" height="30" fill="var(--lime)"/><rect x="280" y="140" width="14" height="12" fill="var(--orange)"/><rect x="300" y="170" width="12" height="12" fill="var(--green)"/><rect x="430" y="240" width="28" height="18" fill="var(--orange)"/>
    <g stroke="var(--navy)" stroke-width="1" fill="none"><line x1="125" y1="152" x2="155" y2="210"/><line x1="125" y1="152" x2="285" y2="146"/><line x1="125" y1="152" x2="305" y2="175"/><line x1="125" y1="152" x2="440" y2="248"/></g>
  </svg>
</section>

<section class="slide dark" style="left:22px;top:1720px">
  <div class="num">37</div>
  <div class="title">Title Example</div>
  <div class="sub">Subtitle Example</div>
  <div class="abs" style="left:0;top:60px;width:565px;height:115px;background:var(--band)"></div>
  <div class="ic" style="left:165px;top:100px;width:24px;height:24px;background:var(--blue)"></div>
  <div class="ic" style="left:287px;top:100px;width:24px;height:24px;background:var(--green)"></div>
  <div class="ic" style="left:409px;top:100px;width:24px;height:24px;background:var(--lime)"></div>
  <div class="abs center" style="left:120px;top:132px;width:115px"><div style="color:#fff;font-size:7px">America</div><p class="p">Donec vel nisl nec risus vulputate placerat in at ligula. Donec auctor magna nec lacus.</p></div>
  <div class="abs center" style="left:242px;top:132px;width:115px"><div style="color:#fff;font-size:7px">Europe</div><p class="p">Donec vel nisl nec risus vulputate placerat in at ligula. Donec auctor magna nec lacus.</p></div>
  <div class="abs center" style="left:364px;top:132px;width:115px"><div style="color:#fff;font-size:7px">Asia</div><p class="p">Donec vel nisl nec risus vulputate placerat in at ligula. Donec auctor magna nec lacus.</p></div>
  <p class="p abs center" style="left:80px;top:240px;width:405px">Donec vel nisl nec risus vulputate placerat in at ligula. Donec auctor magna nec lacus porttitor hendrerit. In pulvinar quam vitae pellentesque aliquam. Fusce venenatis lorem faucibus, commodo magna eget, egestas orci. Nullam at risus congue, hendrerit enim id, dictum dui.</p>
</section>

<section class="slide dark" style="left:612px;top:1720px">
  <div class="num">38</div>
  <svg class="abs" style="left:0;top:0" width="565" height="318"><polygon points="360,318 395,318 565,40 565,0 555,0" fill="var(--green)"/><polygon points="400,318 430,318 565,110 565,60" fill="var(--blue)"/></svg>
  <svg class="sec-icon" viewBox="0 0 24 24"><rect x="1" y="3" width="22" height="14" fill="#fff"/><rect x="3" y="5" width="18" height="10" fill="var(--navy)"/><rect x="9" y="18" width="6" height="3" fill="#fff"/></svg>
  <div class="sec-title">Devices Section</div>
  <div class="sec-sub">Subtitle Example Here</div>
  <p class="p sec-p">Donec vel nisl nec risus vulputate placerat in at ligula. Donec auctor magna nec lacus porttitor hendrerit. In pulvinar quam vitae pellentesque aliquam. Fusce venenatis lorem faucibus, commodo magna eget, egestas orci.</p>
</section>

<section class="slide" style="left:22px;top:2060px">
  <div class="num">39</div>
  <div class="title">Mobil Comparative</div>
  <div class="sub">Subtitle Example</div>
  <div class="ph" role="img" aria-label="Smartphone showing a profile app screen" style="left:40px;top:65px;width:100px;height:215px;border:6px solid #e6e7e9;border-radius:12px;background:linear-gradient(#8a4a3a 25%,#f4f4f4 25%,#f4f4f4 60%,#e9863a 60%,#f4f4f4 65%)"></div>
  <div class="ph" role="img" aria-label="Smartphone showing a photo gallery app screen" style="left:150px;top:65px;width:100px;height:215px;border:6px solid #e6e7e9;border-radius:12px;background:linear-gradient(#8a4a3a 25%,#f4f4f4 25%,#f4f4f4 45%,#5b3a33 45%)"></div>
  <div class="h abs" style="left:300px;top:95px">Title Example</div>
  <p class="p abs" style="left:300px;top:106px;width:230px">Donec vel nisl nec risus vulputate placerat in at ligula. Donec auctor magna nec lacus porttitor hendrerit. In pulvinar quam vitae pellentesque aliquam. Fusce venenatis lorem faucibus.<br><br>Nullam at risus congue, hendrerit enim id, dictum quam. Praesent a tincidunt tortor. Ut malesuada viverra felis quis varius. Nulla facilisi. Etiam molestie risus est.</p>
  <div class="ic" style="left:300px;top:200px;width:22px;height:22px;background:var(--navy)"></div>
  <div class="ic" style="left:332px;top:200px;width:22px;height:22px;background:var(--blue)"></div>
  <div class="ic" style="left:364px;top:200px;width:22px;height:22px;background:var(--green)"></div>
  <div class="ic" style="left:396px;top:200px;width:22px;height:22px;background:var(--lime)"></div>
  <div class="ic" style="left:428px;top:200px;width:22px;height:22px;background:var(--orange)"></div>
</section>

<section class="slide" style="left:612px;top:2060px">
  <div class="num">40</div>
  <div class="abs" style="left:0;top:0;width:565px;height:195px;background:var(--navy)"></div>
  <div class="title light">Mobil user description</div>
  <div class="sub">Subtitle Example</div>
  <div class="ph" role="img" aria-label="Smartphone showing an analytics dashboard" style="left:40px;top:65px;width:100px;height:130px;border:6px solid #e6e7e9;border-bottom:none;border-radius:12px 12px 0 0;background:linear-gradient(#f4f4f4 30%,#6b3a5a 30%,#e9863a 80%,#4a7fb5)"></div>
  <div class="ic" style="left:225px;top:75px;width:22px;height:22px;background:var(--band)"></div>
  <div class="ic" style="left:325px;top:75px;width:22px;height:22px;background:var(--green)"></div>
  <div class="ic" style="left:425px;top:75px;width:22px;height:22px;background:var(--orange)"></div>
  <div class="abs center" style="left:190px;top:110px;width:92px"><div class="h" style="font-size:6px;color:#fff">Title Example</div><p class="p" style="color:#c9ccd2">Donec auctor magna nec lacus porttitor hendrerit. In pulvinar quam vitae.</p></div>
  <div class="abs center" style="left:290px;top:110px;width:92px"><div class="h" style="font-size:6px;color:#fff">Title Example</div><p class="p" style="color:#c9ccd2">Donec auctor magna nec lacus porttitor hendrerit. In pulvinar quam vitae.</p></div>
  <div class="abs center" style="left:390px;top:110px;width:92px"><div class="h" style="font-size:6px;color:#fff">Title Example</div><p class="p" style="color:#c9ccd2">Donec auctor magna nec lacus porttitor hendrerit. In pulvinar quam vitae.</p></div>
  <div class="abs center" style="left:0;top:207px;width:565px;font-size:7px;color:var(--ink)">Conclusion</div>
  <div class="abs center" style="left:0;top:217px;width:565px;font-size:5px;color:var(--green)">Subtitle Example</div>
  <p class="p abs center" style="left:45px;top:230px;width:475px">Donec vel nisl nec risus vulputate placerat in at ligula. Donec auctor magna nec lacus porttitor hendrerit. In pulvinar quam vitae pellentesque aliquam. Fusce venenatis lorem faucibus, commodo magna eget, egestas orci. Nullam at risus congue, hendrerit enim id, dictum quam. Praesent a tincidunt tortor. Ut malesuada viverra felis quis varius. Nulla facilisi. Etiam molestie risus est, at bibendum magna tempus at.</p>
</section>

<section class="slide" style="left:22px;top:2400px">
  <div class="num">41</div>
  <div class="title">Laptop project showcase</div>
  <div class="sub">Subtitle Example</div>
  <div class="ph" role="img" aria-label="Laptop showing a website project" style="left:40px;top:95px;width:210px;height:125px;border:6px solid #2c2f36;border-radius:6px 6px 0 0;background:linear-gradient(#c9452e 35%,#f4f4f4 35%,#f4f4f4 60%,#8a4a3a 60%)"></div>
  <div class="abs" style="left:30px;top:220px;width:230px;height:7px;background:#c4c6ca;border-radius:0 0 6px 6px"></div>
  <div class="h abs" style="left:300px;top:95px">Title Example</div>
  <p class="p abs" style="left:300px;top:106px;width:230px">Donec vel nisl nec risus vulputate placerat in at ligula. Donec auctor magna nec lacus porttitor hendrerit. In pulvinar quam vitae pellentesque aliquam. Fusce venenatis lorem faucibus.<br><br>Nullam at risus congue, hendrerit enim id, dictum quam. Praesent a tincidunt tortor. Ut malesuada viverra felis quis varius. Nulla facilisi. Etiam molestie risus est.</p>
  <div class="ic" style="left:300px;top:200px;width:22px;height:22px;background:var(--navy)"></div>
  <div class="ic" style="left:332px;top:200px;width:22px;height:22px;background:var(--blue)"></div>
  <div class="ic" style="left:364px;top:200px;width:22px;height:22px;background:var(--green)"></div>
  <div class="ic" style="left:396px;top:200px;width:22px;height:22px;background:var(--lime)"></div>
  <div class="ic" style="left:428px;top:200px;width:22px;height:22px;background:var(--orange)"></div>
</section>

<section class="slide" style="left:612px;top:2400px">
  <div class="num">42</div>
  <div class="title">App description</div>
  <div class="sub">Subtitle Example</div>
  <div class="ph" role="img" aria-label="Smartphone showing a user profile app" style="left:30px;top:65px;width:105px;height:215px;border:6px solid #e6e7e9;border-radius:12px;background:linear-gradient(#c9452e 12%,#f4f4f4 12%,#f4f4f4 70%,#6dbf96 70%,#f4f4f4 76%)"></div>
  <svg class="abs" style="left:0;top:0" width="565" height="318"><g stroke="#b5b9bf" stroke-width=".6" fill="none">
    <path d="M145,170 H250 V75 H270"/><path d="M145,172 H260 V125 H325"/><path d="M145,174 H310 V175 H325"/><path d="M145,176 H260 V225 H325"/><path d="M145,178 H250 V270 H270"/></g></svg>
  <div class="ic" style="left:270px;top:65px;width:20px;height:20px;background:var(--navy)"></div>
  <div class="abs" style="left:295px;top:63px;width:230px"><div class="h" style="font-size:6px">Title Example</div><p class="p">Lorem ipsum dolor sit amet, consectetur adipiscing elit. Fusce diam tortor, mattis quis dapibus vitae.</p></div>
  <div class="ic" style="left:325px;top:115px;width:20px;height:20px;background:var(--blue)"></div>
  <div class="abs" style="left:350px;top:113px;width:175px"><div class="h" style="font-size:6px">Title Example</div><p class="p">Lorem ipsum dolor sit amet, consectetur adipiscing elit. Fusce diam tortor, mattis quis dapibus vitae.</p></div>
  <div class="ic" style="left:325px;top:165px;width:20px;height:20px;background:var(--green)"></div>
  <div class="abs" style="left:350px;top:163px;width:175px"><div class="h" style="font-size:6px">Title Example</div><p class="p">Lorem ipsum dolor sit amet, consectetur adipiscing elit. Fusce diam tortor, mattis quis dapibus vitae.</p></div>
  <div class="ic" style="left:325px;top:215px;width:20px;height:20px;background:var(--lime)"></div>
  <div class="abs" style="left:350px;top:213px;width:175px"><div class="h" style="font-size:6px">Title Example</div><p class="p">Lorem ipsum dolor sit amet, consectetur adipiscing elit. Fusce diam tortor, mattis quis dapibus vitae.</p></div>
  <div class="ic" style="left:270px;top:260px;width:20px;height:20px;background:var(--orange)"></div>
  <div class="abs" style="left:295px;top:258px;width:230px"><div class="h" style="font-size:6px">Title Example</div><p class="p">Lorem ipsum dolor sit amet, consectetur adipiscing elit. Fusce diam tortor, mattis quis dapibus vitae.</p></div>
</section>

<section class="slide" style="left:22px;top:2740px">
  <div class="num">43</div>
  <div class="abs" style="left:0;top:0;width:565px;height:195px;background:var(--navy)"></div>
  <div class="title light">Mobil user description</div>
  <div class="sub">Subtitle Example</div>
  <div class="ph" role="img" aria-label="Smartphone showing a shop app" style="left:40px;top:65px;width:100px;height:130px;border:6px solid #e6e7e9;border-bottom:none;border-radius:12px 12px 0 0;background:linear-gradient(#f4f4f4 20%,#c9452e 20%,#c9452e 50%,#f4f4f4 50%)"></div>
  <svg class="abs" style="left:180px;top:70px" width="360" height="110">
    <g stroke="#4b5468" stroke-width=".5"><line x1="20" y1="10" x2="360" y2="10"/><line x1="20" y1="25" x2="360" y2="25"/><line x1="20" y1="40" x2="360" y2="40"/><line x1="20" y1="55" x2="360" y2="55"/><line x1="20" y1="70" x2="360" y2="70"/><line x1="20" y1="85" x2="360" y2="85"/></g>
    <g fill="#8a8f97" font-size="6" font-family="Lato,sans-serif"><text x="0" y="12">70</text><text x="0" y="27">60</text><text x="0" y="42">50</text><text x="0" y="57">30</text><text x="0" y="72">10</text><text x="3" y="87">0</text><text x="25" y="100">Abril</text><text x="130" y="100">Mayo</text><text x="235" y="100">Junio</text><text x="330" y="100">Julio</text></g>
    <polyline points="25,55 130,30 235,60 350,15" stroke="var(--green)" stroke-width="1.3" fill="none"/>
    <polyline points="25,40 130,62 235,40 350,55" stroke="var(--lime)" stroke-width="1.3" fill="none"/>
    <polyline points="25,70 130,50 235,30 350,42" stroke="var(--blue)" stroke-width="1.3" fill="none"/>
  </svg>
  <div class="abs center" style="left:0;top:207px;width:565px;font-size:7px;color:var(--ink)">Conclusion</div>
  <div class="abs center" style="left:0;top:217px;width:565px;font-size:5px;color:var(--green)">Subtitle Example</div>
  <p class="p abs center" style="left:45px;top:230px;width:475px">Donec vel nisl nec risus vulputate placerat in at ligula. Donec auctor magna nec lacus porttitor hendrerit. In pulvinar quam vitae pellentesque aliquam. Fusce venenatis lorem faucibus, commodo magna eget, egestas orci. Nullam at risus congue, hendrerit enim id, dictum quam. Ut malesuada viverra felis quis varius. Nulla facilisi. Etiam molestie risus est, at bibendum magna tempus at.</p>
</section>

<section class="slide" style="left:612px;top:2740px">
  <div class="num">44</div>
  <div class="title" style="top:40px">Tablet project description</div>
  <div class="sub" style="top:58px">Subtitle Example</div>
  <div class="ph" role="img" aria-label="Tablet showing a restaurant website" style="left:40px;top:90px;width:220px;height:228px;border:8px solid #1e2127;border-bottom:none;border-radius:10px 10px 0 0;background:linear-gradient(#5b1e1e 20%,#f2eee6 20%,#f2eee6 55%,#8a4a3a 55%,#f2eee6 80%)"></div>
  <div class="h abs" style="left:300px;top:110px">Title Example</div>
  <p class="p abs" style="left:300px;top:121px;width:230px">Donec vel nisl nec risus vulputate placerat in at ligula. Donec auctor magna nec lacus porttitor hendrerit. In pulvinar quam vitae pellentesque aliquam. Fusce venenatis lorem faucibus.<br><br>Nullam at risus congue, hendrerit enim id, dictum quam. Praesent a tincidunt tortor. Ut malesuada viverra felis quis varius. Nulla facilisi. Etiam molestie risus est.</p>
  <div class="ic" style="left:300px;top:215px;width:22px;height:22px;background:var(--navy)"></div>
  <div class="ic" style="left:332px;top:215px;width:22px;height:22px;background:var(--blue)"></div>
  <div class="ic" style="left:364px;top:215px;width:22px;height:22px;background:var(--green)"></div>
  <div class="ic" style="left:396px;top:215px;width:22px;height:22px;background:var(--lime)"></div>
  <div class="ic" style="left:428px;top:215px;width:22px;height:22px;background:var(--orange)"></div>
</section>

<section class="slide dark" style="left:22px;top:3080px">
  <div class="num">45</div>
  <svg class="abs" style="left:0;top:0" width="565" height="318"><polygon points="360,318 395,318 565,40 565,0 555,0" fill="var(--green)"/><polygon points="400,318 430,318 565,110 565,60" fill="var(--blue)"/></svg>
  <svg class="sec-icon" viewBox="0 0 24 24"><path d="M12 12 V1 A11 11 0 1 1 1 12 Z" fill="#fff"/><path d="M10 10 V0 A10 10 0 0 0 0 10 Z" fill="#fff"/></svg>
  <div class="sec-title">Utilitys</div>
  <div class="sec-sub">Subtitle Example Here</div>
  <p class="p sec-p">Donec vel nisl nec risus vulputate placerat in at ligula. Donec auctor magna nec lacus porttitor hendrerit. In pulvinar quam vitae pellentesque aliquam. Fusce venenatis lorem faucibus, commodo magna eget, egestas orci.</p>
</section>

<section class="slide" style="left:612px;top:3080px">
  <div class="num">46</div>
  <div class="title" style="top:40px">Triple Graph Example</div>
  <div class="sub" style="top:58px">Subtitle Example</div>
  <svg class="abs" style="left:0;top:0" width="565" height="318" font-family="Lato,sans-serif">
    <g font-size="5" fill="#8a8f97">
      <text x="20" y="92">100%</text><text x="24" y="109">75%</text><text x="24" y="126">50%</text><text x="24" y="143">25%</text><text x="28" y="160">0%</text>
      <text x="190" y="92">100%</text><text x="194" y="109">75%</text><text x="194" y="126">50%</text><text x="194" y="143">25%</text><text x="198" y="160">0%</text>
      <text x="360" y="92">100%</text><text x="364" y="109">75%</text><text x="364" y="126">50%</text><text x="364" y="143">25%</text><text x="368" y="160">0%</text>
    </g>
    <g fill="#b9bcc1">
      <rect x="45" y="90" width="9" height="68"/><rect x="60" y="90" width="9" height="68"/><rect x="75" y="90" width="9" height="68"/><rect x="90" y="90" width="9" height="68"/><rect x="105" y="90" width="9" height="68"/><rect x="120" y="90" width="9" height="68"/><rect x="135" y="90" width="9" height="68"/>
      <rect x="215" y="90" width="9" height="68"/><rect x="230" y="90" width="9" height="68"/><rect x="245" y="90" width="9" height="68"/><rect x="260" y="90" width="9" height="68"/><rect x="275" y="90" width="9" height="68"/><rect x="290" y="90" width="9" height="68"/><rect x="305" y="90" width="9" height="68"/>
      <rect x="385" y="90" width="9" height="68"/><rect x="400" y="90" width="9" height="68"/><rect x="415" y="90" width="9" height="68"/><rect x="430" y="90" width="9" height="68"/><rect x="445" y="90" width="9" height="68"/><rect x="460" y="90" width="9" height="68"/><rect x="475" y="90" width="9" height="68"/>
    </g>
    <g fill="var(--navy)"><rect x="45" y="120" width="9" height="38"/><rect x="60" y="110" width="9" height="48"/><rect x="75" y="130" width="9" height="28"/><rect x="90" y="105" width="9" height="53"/><rect x="105" y="125" width="9" height="33"/><rect x="120" y="115" width="9" height="43"/><rect x="135" y="128" width="9" height="30"/></g>
    <g fill="var(--blue)"><rect x="215" y="125" width="9" height="33"/><rect x="230" y="108" width="9" height="50"/><rect x="245" y="118" width="9" height="40"/><rect x="260" y="130" width="9" height="28"/><rect x="275" y="112" width="9" height="46"/><rect x="290" y="122" width="9" height="36"/><rect x="305" y="106" width="9" height="52"/></g>
    <g fill="var(--green)"><rect x="385" y="115" width="9" height="43"/><rect x="400" y="128" width="9" height="30"/><rect x="415" y="108" width="9" height="50"/><rect x="430" y="120" width="9" height="38"/><rect x="445" y="132" width="9" height="26"/><rect x="460" y="112" width="9" height="46"/><rect x="475" y="125" width="9" height="33"/></g>
    <circle cx="95" cy="185" r="10" fill="var(--navy)"/><circle cx="265" cy="185" r="10" fill="var(--green)"/><circle cx="435" cy="185" r="10" fill="var(--orange)"/>
  </svg>
  <p class="p abs center" style="left:30px;top:205px;width:130px">Donec vel nisl nec risus vulputate placerat in at ligula. Donec auctor magna nec lacus porttitor hendrerit. In pulvinar quam vitae.</p>
  <p class="p abs center" style="left:200px;top:205px;width:130px">Donec vel nisl nec risus vulputate placerat in at ligula. Donec auctor magna nec lacus porttitor hendrerit. In pulvinar quam vitae.</p>
  <p class="p abs center" style="left:370px;top:205px;width:130px">Donec vel nisl nec risus vulputate placerat in at ligula. Donec auctor magna nec lacus porttitor hendrerit. In pulvinar quam vitae.</p>
</section>

<section class="slide" style="left:22px;top:3420px">
  <div class="num">47</div>
  <div class="title">Five circles diagram</div>
  <div class="sub">Subtitle Example</div>
  <svg class="abs" style="left:0;top:0" width="565" height="318" font-family="Lato,sans-serif">
    <circle cx="282" cy="135" r="50" fill="none" stroke="#e6e7e9" stroke-width="2"/>
    <circle cx="282" cy="85" r="24" fill="var(--red)"/><circle cx="330" cy="120" r="24" fill="var(--blue)"/><circle cx="312" cy="178" r="24" fill="var(--green)"/><circle cx="252" cy="178" r="24" fill="var(--lime)"/><circle cx="234" cy="120" r="24" fill="var(--orange)"/>
    <g fill="#fff" font-size="5" text-anchor="middle"><text x="282" y="84">Title</text><text x="282" y="91">example</text><text x="330" y="119">Title</text><text x="330" y="126">example</text><text x="312" y="177">Title</text><text x="312" y="184">example</text><text x="252" y="177">Title</text><text x="252" y="184">example</text><text x="234" y="119">Title</text><text x="234" y="126">example</text></g>
    <rect x="105" y="100" width="16" height="12" rx="2" fill="none" stroke="var(--blue)" stroke-width="1.4"/><line x1="105" y1="104" x2="121" y2="104" stroke="var(--blue)" stroke-width="1.4"/>
    <rect x="445" y="100" width="16" height="12" rx="1" fill="none" stroke="var(--blue)" stroke-width="1.4"/><line x1="453" y1="100" x2="453" y2="112" stroke="var(--blue)"/>
  </svg>
  <div class="abs center" style="left:55px;top:120px;width:115px"><div style="color:var(--blue);font-size:6px">Subtitle Example</div><p class="p">Lorem ipsum dolor sit amet, consectetur adipiscing elit. Fusce diam tortor, mattis quis dapibus vitae, euismod non purus.</p></div>
  <div class="abs center" style="left:395px;top:120px;width:115px"><div style="color:var(--blue);font-size:6px">Subtitle Example</div><p class="p">Lorem ipsum dolor sit amet, consectetur adipiscing elit. Fusce diam tortor, mattis quis dapibus vitae, euismod non purus.</p></div>
  <p class="p abs center" style="left:45px;top:255px;width:475px">Lorem ipsum dolor sit amet, consectetur adipiscing elit. Fusce diam tortor, mattis quis dapibus vitae, euismod non purus. Maecenas at lacus nec mauris feugiat. Duis tempus eros et orci tempus semper. Nullam finibus nisl id ligula vestibulum, ut semper ex suscipit. Cras fringilla suscipit purus.</p>
</section>

<section class="slide" style="left:612px;top:3420px">
  <div class="num">48</div>
  <div class="title">Pie chart slide</div>
  <div class="sub">Subtitle Example</div>
  <p class="p abs" style="left:40px;top:55px;width:485px">Donec vel nisl nec risus vulputate placerat in at ligula. Donec auctor magna nec lacus porttitor hendrerit. In pulvinar quam vitae pellentesque aliquam. Fusce venenatis lorem faucibus, commodo magna eget, egestas orci. Nullam at risus congue, hendrerit enim id, dictum quam. Praesent a tincidunt tortor. Ut malesuada viverra felis quis varius. Nulla facilisi.</p>
  <svg class="abs" style="left:0;top:0" width="565" height="318" font-family="Lato,sans-serif">
    <g opacity=".95">
      <path d="M30,210 C55,210 55,140 78,140 C101,140 101,210 126,210 Z" fill="var(--orange)"/>
      <path d="M70,210 C95,210 95,130 118,130 C141,130 141,210 166,210 Z" fill="var(--blue)"/>
      <path d="M115,210 C140,210 140,150 163,150 C186,150 186,210 211,210 Z" fill="var(--green)"/>
      <path d="M160,210 C185,210 185,125 208,125 C231,125 231,210 256,210 Z" fill="var(--lime)"/>
      <path d="M205,210 C230,210 230,145 253,145 C276,145 276,210 301,210 Z" fill="var(--green)"/>
      <path d="M250,210 C275,210 275,130 298,130 C321,130 321,210 346,210 Z" fill="var(--red)"/>
      <path d="M295,210 C320,210 320,155 343,155 C366,155 366,210 391,210 Z" fill="var(--orange)"/>
      <path d="M340,210 C365,210 365,132 388,132 C411,132 411,210 436,210 Z" fill="var(--navy)"/>
      <path d="M385,210 C410,210 410,150 433,150 C456,150 456,210 481,210 Z" fill="var(--green)"/>
      <path d="M430,210 C455,210 455,160 478,160 C501,160 501,210 526,210 Z" fill="var(--orange)"/>
    </g>
    <g font-size="6" text-anchor="middle"><text x="78" y="135" fill="var(--orange)">57%</text><text x="118" y="125" fill="var(--blue)">75%</text><text x="163" y="145" fill="var(--green)">82%</text><text x="208" y="120" fill="var(--lime)">47%</text><text x="253" y="140" fill="var(--green)">61%</text><text x="298" y="125" fill="var(--red)">46%</text><text x="343" y="150" fill="var(--orange)">71%</text><text x="388" y="127" fill="var(--navy)">67%</text><text x="478" y="155" fill="var(--orange)">77%</text></g>
  </svg>
  <div class="abs center" style="left:40px;top:225px;width:110px"><div class="h" style="font-size:6px">Honduras</div><p class="p">Donec vel nisl nec risus vulputate placerat in at ligula auctor magna nec.</p></div>
  <div class="abs center" style="left:160px;top:225px;width:110px"><div class="h" style="font-size:6px">India</div><p class="p">Donec vel nisl nec risus vulputate placerat in at ligula auctor magna nec.</p></div>
  <div class="abs center" style="left:290px;top:225px;width:110px"><div class="h" style="font-size:6px">United States</div><p class="p">Donec vel nisl nec risus vulputate placerat in at ligula auctor magna nec.</p></div>
  <div class="abs center" style="left:415px;top:225px;width:110px"><div class="h" style="font-size:6px">Spain</div><p class="p">Donec vel nisl nec risus vulputate placerat in at ligula auctor magna nec.</p></div>
</section>

<section class="slide" style="left:22px;top:3760px">
  <div class="num">49</div>
  <div class="title">Simple process SmartArt</div>
  <div class="sub">Subtitle Example</div>
  <p class="p abs center" style="left:45px;top:55px;width:475px">Lorem ipsum dolor sit amet, consectetur adipiscing elit. Fusce diam tortor, mattis quis dapibus vitae, euismod non purus. Maecenas at lacus nec mauris feugiat. Duis tempus eros et orci tempus semper. Nullam finibus nisl id ligula vestibulum, ut semper ex suscipit. Cras fringilla suscipit purus.</p>
  <svg class="abs" style="left:0;top:0" width="565" height="318">
    <polygon points="55,115 125,115 125,125 135,135 125,145 125,165 55,165" fill="var(--blue)"/>
    <polygon points="180,115 250,115 250,125 260,135 250,145 250,165 180,165" fill="var(--green)"/>
    <polygon points="305,115 375,115 375,125 385,135 375,145 375,165 305,165" fill="var(--lime)"/>
    <rect x="430" y="115" width="75" height="50" fill="var(--orange)"/>
    <g fill="#fff"><rect x="84" y="134" width="12" height="8"/><circle cx="215" cy="140" r="6"/><rect x="334" y="134" width="12" height="8"/><rect x="461" y="134" width="12" height="10"/></g>
  </svg>
  <div class="abs center" style="left:45px;top:178px;width:95px"><div style="color:var(--blue);font-size:6px">Subtitle Example</div><p class="p">Lorem ipsum dolor sit amet, consectetur adipiscing elit. Fusce diam tortor, mattis quis dapibus vitae, euismod non purus.</p></div>
  <div class="abs center" style="left:170px;top:178px;width:95px"><div style="color:var(--blue);font-size:6px">Subtitle Example</div><p class="p">Lorem ipsum dolor sit amet, consectetur adipiscing elit. Fusce diam tortor, mattis quis dapibus vitae, euismod non purus.</p></div>
  <div class="abs center" style="left:295px;top:178px;width:95px"><div style="color:var(--blue);font-size:6px">Subtitle Example</div><p class="p">Lorem ipsum dolor sit amet, consectetur adipiscing elit. Fusce diam tortor, mattis quis dapibus vitae, euismod non purus.</p></div>
  <div class="abs center" style="left:420px;top:178px;width:95px"><div style="color:var(--blue);font-size:6px">Subtitle Example</div><p class="p">Lorem ipsum dolor sit amet, consectetur adipiscing elit. Fusce diam tortor, mattis quis dapibus vitae, euismod non purus.</p></div>
</section>

<section class="slide" style="left:612px;top:3760px">
  <div class="num">50</div>
  <div class="abs center" style="left:0;top:48px;width:565px;font-size:12px;color:var(--ink)">Analysis</div>
  <div class="abs center" style="left:0;top:66px;width:565px;font-size:86px;font-weight:700;color:var(--band);line-height:1">SWOT</div>
  <div class="abs" style="left:45px;top:180px;font-size:24px;color:var(--band)">S</div>
  <div class="abs" style="left:75px;top:180px;width:190px"><div class="h" style="font-size:6px;font-weight:400">Subtitle Example</div><p class="p">Donec vel nisl nec risus vulputate placerat in at ligula magna nec lacus porttitor hendrerit. In pulvinar quam vitae pel erit lorem.</p></div>
  <div class="abs" style="left:300px;top:180px;font-size:24px;color:var(--blue)">W</div>
  <div class="abs" style="left:335px;top:180px;width:190px"><div class="h" style="font-size:6px;font-weight:400">Subtitle Example</div><p class="p">Donec vel nisl nec risus vulputate placerat in at ligula magna nec lacus porttitor hendrerit. In pulvinar quam vitae pel erit lorem.</p></div>
  <div class="abs" style="left:45px;top:245px;font-size:24px;color:var(--green)">O</div>
  <div class="abs" style="left:75px;top:245px;width:190px"><div class="h" style="font-size:6px;font-weight:400">Subtitle Example</div><p class="p">Donec vel nisl nec risus vulputate placerat in at ligula magna nec lacus porttitor hendrerit. In pulvinar quam vitae pel erit lorem.</p></div>
  <div class="abs" style="left:305px;top:245px;font-size:24px;color:var(--lime)">T</div>
  <div class="abs" style="left:335px;top:245px;width:190px"><div class="h" style="font-size:6px;font-weight:400">Subtitle Example</div><p class="p">Donec vel nisl nec risus vulputate placerat in at ligula magna nec lacus porttitor hendrerit. In pulvinar quam vitae pel erit lorem.</p></div>
</section>

<section class="slide dark" style="left:22px;top:4100px">
  <div class="num">51</div>
  <svg class="abs" style="left:0;top:0" width="565" height="318"><polygon points="360,318 395,318 565,40 565,0 555,0" fill="var(--green)"/><polygon points="400,318 430,318 565,110 565,60" fill="var(--blue)"/></svg>
  <svg class="sec-icon" viewBox="0 0 24 24"><path d="M3 6 H17 V14 A5 5 0 0 1 12 19 H8 A5 5 0 0 1 3 14 Z" fill="#fff"/><path d="M17 8 H20 A2 2 0 0 1 20 13 H17" stroke="#fff" stroke-width="2" fill="none"/><rect x="2" y="21" width="16" height="2" fill="#fff"/></svg>
  <div class="sec-title">Grab a Coffe</div>
  <div class="sec-sub">Subtitle Example</div>
  <p class="p sec-p">Donec vel nisl nec risus vulputate placerat in at ligula. Donec auctor magna nec lacus porttitor hendrerit. In pulvinar quam vitae pellentesque aliquam. Fusce venenatis lorem faucibus, commodo magna eget, egestas orci.</p>
</section>

<section class="slide" style="left:612px;top:4100px">
  <div class="num">52</div>
  <div class="title">Arrow process SmartArt</div>
  <div class="sub">Subtitle Example</div>
  <p class="p abs center" style="left:45px;top:55px;width:475px">Lorem ipsum dolor sit amet, consectetur adipiscing elit. Fusce diam tortor, mattis quis dapibus vitae, euismod non purus. Maecenas at lacus nec mauris feugiat. Duis tempus eros et orci tempus semper. Nullam finibus nisl id ligula vestibulum, ut semper ex suscipit.</p>
  <div class="abs" style="left:65px;top:100px;width:55px;height:55px;background:var(--blue);color:#cfe0f2;font-size:11px;text-align:center;padding-top:12px;line-height:1.2">First<br>Steep</div>
  <div class="abs" style="left:190px;top:100px;width:55px;height:55px;background:var(--green);color:#d9f0e4;font-size:11px;text-align:center;padding-top:12px;line-height:1.2">Second<br>Steep</div>
  <div class="abs" style="left:315px;top:100px;width:55px;height:55px;background:var(--lime);color:#e6f2c6;font-size:11px;text-align:center;padding-top:12px;line-height:1.2">Third<br>Steep</div>
  <div class="abs" style="left:440px;top:100px;width:55px;height:55px;background:var(--orange);color:#fbdcc2;font-size:11px;text-align:center;padding-top:12px;line-height:1.2">Fourth<br>Steep</div>
  <svg class="abs" style="left:0;top:0" width="565" height="318">
    <g fill="var(--navy)"><polygon points="150,123 158,128 150,133"/><polygon points="275,123 283,128 275,133"/><polygon points="400,123 408,128 400,133"/><rect x="144" y="126" width="6" height="4"/><rect x="269" y="126" width="6" height="4"/><rect x="394" y="126" width="6" height="4"/></g>
    <polygon points="86,170 98,176 86,182 89,176" fill="var(--blue)"/>
    <circle cx="217" cy="176" r="6" fill="var(--green)"/>
    <rect x="337" y="170" width="10" height="12" fill="var(--lime)"/>
    <rect x="462" y="170" width="12" height="12" fill="var(--orange)"/>
  </svg>
  <div class="abs center" style="left:45px;top:190px;width:95px"><div style="color:var(--blue);font-size:6px">Subtitle Example</div><p class="p">Lorem ipsum dolor sit amet, consectetur adipiscing elit. Fusce diam tortor, mattis quis dapibus vitae, euismod non purus.</p></div>
  <div class="abs center" style="left:170px;top:190px;width:95px"><div style="color:var(--blue);font-size:6px">Subtitle Example</div><p class="p">Lorem ipsum dolor sit amet, consectetur adipiscing elit. Fusce diam tortor, mattis quis dapibus vitae, euismod non purus.</p></div>
  <div class="abs center" style="left:295px;top:190px;width:95px"><div style="color:var(--blue);font-size:6px">Subtitle Example</div><p class="p">Lorem ipsum dolor sit amet, consectetur adipiscing elit. Fusce diam tortor, mattis quis dapibus vitae, euismod non purus.</p></div>
  <div class="abs center" style="left:420px;top:190px;width:95px"><div style="color:var(--blue);font-size:6px">Subtitle Example</div><p class="p">Lorem ipsum dolor sit amet, consectetur adipiscing elit. Fusce diam tortor, mattis quis dapibus vitae, euismod non purus.</p></div>
</section>

</body>
</html>
```